Wordpress Design Project - Australian Solar Company wants to start FRESH!

About us

Bright Meadow are a renewable energy company based in Perth Australia, but we also have offices all over Asia. We specialise in offering renewable energy solutions (Solar PV Systems and LED Lighting) to residential and commercial customers.

Our current website: www.brightmeadowenergy.com.au

Our needs

This will be a replacement website as we are not happy with our current layout. We have an Australian company doing our SEO and they have recommended a new layout which we wish to go with.

We really want a professional and easy to navigate website that will assist in bringing in more enquiries and phone calls.

Content

We have all the content and will get the design winner to add this after we have chosen the design we like.
It is important that the call to actions are presented well and are visible these are things like the free quote form and our phone number.

The layout as we have advised has been based on SEO research so we wish it to be exactly the same unless otherwise stated.

Call to action

Our main objective of the new website is for people to come to the home page and see us as a professional and reliable company to deal with and enquire further.

We really want as many people as we can to convert to a lead. We want every person that comes to the website to enquire online or call us. We feel it is important to have a contact us/quote form on every page of the website.

Functional requirements

We have a chatterbook and vidstream account so links to these would be needed

Design assets

The logo needs to be displayed as shown in the website layout brief

Colours – we would like fresh, subdued colours that are professional and appealing to the eye. We ask that you do not take the colours from the logo.

Current website dislikes – the things we currently dislike about our current website is that it is hard to find information and there is no clear call to action. The colours are really unappealing as well as it looks cheap not professional.
The graphics that we require for the slider on the home page will have to be given after the winner is chosen but we want there to be three sliders on rotation

- Credibility builder (employee infront of solar panel) that encourages we use all our own employees not subcontractors
- Residential Slider – picture of a couple and solar panel system with a testimonial
- Commercial slider – picture of commercial system with “find out how you can install solar for free* at your business”

Design ideas

The website needs to be mobile friendly as well
It is going to be a total rebuild from the current website as our current website really isn’t working for us.

Target Market(s)

Target Audience

Our target audience are both residential and commercial clients
Residential – we want to attract home owners that are interested in reducing their electricity bill and helping the environment. Generally these people are between the ages of 28-50+ both male and female.

Commercial – We want to appeal to key decision makers within the commercial sphere. For example – CEOs, Company Directors, Operation managers and business owners of any industry. These people will be interested in reducing their electricity bills and creating a clean green image for their business.
Our target audience will generally come to our website to get information and enquire for a quote/ product information.

Industry/Entity Type

Residential

Requirements
Must have
• MUST BE LAID OUT LIKE THIS:

http://www.docuvault.com/doc/849302715/Website-Layout

Must have Enquire Now forms on every page that read:

Name
Phone Number
How did you hear about us
Message

```html
<!DOCTYPE html>
<html lang="en">
<head>
<meta charset="utf-8">
<title>Bright Meadow – Solar Power Perth</title>
<link href="https://fonts.googleapis.com/css2?family=Arimo:wght@400;700&display=swap" rel="stylesheet">
<style>
:root{
  --green:#3f8f1f;
  --green-dark:#2c6a12;
  --green-deep:#1f4d0c;
  --yellow:#f6c617;
  --yellow-soft:#f9d648;
  --red:#d62020;
  --sky:#3b8ed8;
  --sky-light:#bfe0f7;
  --grey:#ececec;
  --ink:#333;
  --white:#fff;
}
*{box-sizing:border-box;margin:0;padding:0}
html,body{width:816px;height:1200px;overflow:hidden}
body{font-family:"Arimo",Arial,sans-serif;color:var(--ink);background:var(--white);position:relative}
.header{position:absolute;left:0;top:0;width:816px;height:87px;background:var(--white)}
.brand{position:absolute;left:40px;top:10px;display:flex;align-items:center;gap:10px}
.brand-dot{width:34px;height:34px;border-radius:50%;background:var(--yellow)}
.brand-name{font-size:26px;font-weight:700;color:var(--green)}
.call{position:absolute;right:40px;top:12px;display:flex;align-items:center;gap:8px}
.call-photo{width:32px;height:40px;border-radius:4px;background:linear-gradient(#e8d2c0,#7a5a48)}
.call-pill{background:var(--red);color:var(--white);font-weight:700;font-size:16px;padding:7px 14px;border-radius:14px;display:flex;align-items:center;gap:6px}
.nav{position:absolute;right:40px;top:60px;display:flex;gap:3px}
.nav a{display:block;background:var(--green);color:var(--white);font-size:11px;font-weight:700;text-decoration:none;padding:7px 12px;border-radius:4px 4px 0 0}
.nav a.active{background:var(--yellow);color:var(--green-deep)}
.hero{position:absolute;left:0;top:87px;width:816px;height:267px;background:linear-gradient(180deg,var(--sky) 0%,var(--sky-light) 60%,#7fb04a 100%);overflow:hidden}
.hero-person{position:absolute;left:90px;top:30px;width:130px;height:237px;background:linear-gradient(#3a3f4a,#1c2026);border-radius:60px 60px 0 0}
.hero-copy{position:absolute;left:230px;top:40px;width:330px}
.hero-title{font-size:40px;font-weight:700;color:var(--yellow);line-height:1}
.hero-title small{font-size:24px;color:var(--white);font-weight:700}
.hero-text{margin-top:10px;color:var(--white);font-size:15px;font-weight:700;line-height:1.3}
.hero-btn{display:inline-block;margin-top:16px;background:var(--red);color:var(--white);font-weight:700;font-size:14px;padding:9px 16px;border-radius:4px}
.arrow{position:absolute;top:120px;width:26px;height:26px;border-radius:50%;background:rgba(255,255,255,.85)}
.arrow.l{left:10px}.arrow.r{right:10px}
.quote{position:absolute;right:40px;top:10px;width:185px;height:245px;background:rgba(255,255,255,.92);border:1px solid #ccc;padding:0 10px}
.quote h3{background:var(--green);color:var(--white);font-size:11px;text-align:center;padding:6px;margin:0 -10px 8px}
.field{display:flex;align-items:center;margin-bottom:6px;font-size:10px}
.field span{width:50px}
.field i{flex:1;height:16px;border:1px solid #bbb;background:var(--white)}
.quote label{font-size:10px}
.quote .area{height:58px;border:1px solid #bbb;background:var(--white);margin-top:4px}
.submit{display:block;margin:8px auto 0;width:70px;background:var(--yellow);text-align:center;font-size:11px;font-weight:700;padding:5px;border-radius:3px}
.cards{position:absolute;left:0;top:354px;width:816px;height:296px;background:var(--grey);display:flex;justify-content:center;gap:14px;padding-top:22px}
.card{width:170px;text-align:center}
.card-art{height:90px;background:var(--white);border:1px solid #ddd;display:flex;align-items:center;justify-content:center}
.card-art div{width:70px;height:60px;border-radius:6px}
.card h4{color:var(--green);font-size:15px;margin:10px 0 6px;line-height:1.2}
.card p{font-size:10px;line-height:1.4;text-align:left}
.more{display:inline-block;margin-top:8px;background:var(--yellow);font-size:10px;font-weight:700;padding:4px 10px;border-radius:3px;float:left}
.welcome{position:absolute;left:0;top:650px;width:816px;height:290px;background:var(--green)}
.welcome-copy{position:absolute;left:40px;top:22px;width:440px;color:var(--white)}
.welcome-copy h2{color:var(--yellow);font-size:28px;margin-bottom:12px}
.welcome-copy p{font-size:11px;line-height:1.5;margin-bottom:10px}
.testimonial{position:absolute;right:40px;top:22px;width:270px;height:240px;background:#111;border:1px solid #555}
.testimonial h5{color:var(--white);font-size:12px;padding:6px 8px}
.video{margin:0 8px;height:182px;background:linear-gradient(#2a2a2a,#555)}
.controls{height:22px;margin:6px 8px;background:#333;display:flex;align-items:center;padding:0 8px;gap:8px}
.controls b{width:0;height:0;border-left:8px solid var(--white);border-top:5px solid transparent;border-bottom:5px solid transparent}
.controls i{flex:1;height:4px;background:#888}
.promo{position:absolute;left:0;top:940px;width:816px;height:215px;background:linear-gradient(90deg,var(--yellow-soft),var(--yellow))}
.services{position:absolute;left:40px;top:18px;width:220px;height:180px;background:var(--white);padding:12px 14px;border-radius:4px}
.services h4{color:var(--green);font-size:13px;margin-bottom:8px}
.services li{list-style:none;font-size:11px;margin-bottom:4px;display:flex;align-items:center;gap:6px}
.services li::before{content:"";width:7px;height:7px;border-radius:50%;background:var(--green)}
.cta{position:absolute;top:40px;width:130px;text-align:center}
.cta-circle{width:110px;height:110px;margin:0 auto;border-radius:50%;background:var(--white);border:3px solid var(--red);display:flex;flex-direction:column;align-items:center;justify-content:center;font-weight:700}
.cta-circle .small{font-size:11px}
.cta-circle .big{font-size:18px;color:var(--red)}
.cta-btn{display:inline-block;margin-top:8px;background:var(--red);color:var(--white);font-size:11px;font-weight:700;padding:5px 12px;border-radius:3px}
.contact{position:absolute;right:40px;top:18px;width:230px;height:180px;background:var(--white);padding:12px;border-radius:4px;font-size:10px;line-height:1.5}
.contact p{margin-bottom:6px}
.contact b{color:var(--green)}
.footer{position:absolute;left:0;top:1155px;width:816px;height:45px;background:var(--green-deep);color:#cfe3c2;font-size:10px;text-align:center;padding-top:16px}
</style>
</head>
<body>
<header class="header">
  <div class="brand"><span class="brand-dot"></span><span class="brand-name">Bright Meadow</span></div>
  <div class="call">
    <div class="call-photo" role="img" aria-label="Photo of a customer service representative"></div>
    <div class="call-pill">
      <svg width="14" height="14" viewBox="0 0 24 24"><path fill="#fff" d="M6.6 10.8a15 15 0 0 0 6.6 6.6l2.2-2.2c.3-.3.7-.4 1-.2 1.1.4 2.3.6 3.6.6.6 0 1 .4 1 1V20c0 .6-.4 1-1 1A17 17 0 0 1 3 4c0-.6.4-1 1-1h3.5c.6 0 1 .4 1 1 0 1.3.2 2.5.6 3.6.1.3 0 .7-.2 1z"/></svg>
      Call Now: 1300 555 014
    </div>
  </div>
  <nav class="nav">
    <a class="active" href="#">ABOUT US</a><a href="#">PRODUCTS</a><a href="#">SERVICES</a><a href="#">WHY BRIGHT MEADOW</a><a href="#">CONTACT</a>
  </nav>
</header>

<section class="hero" role="img" aria-label="Solar panels under a blue sky">
  <div class="hero-person" role="img" aria-label="Employee in a suit standing in front of solar panels"></div>
  <div class="hero-copy">
    <div class="hero-title">Solar <small>Photovoltaic</small></div>
    <p class="hero-text">All our home Solar Panels are of high quality with long lifetime guarantees.</p>
    <span class="hero-btn">Click Here to Know More</span>
  </div>
  <span class="arrow l"></span><span class="arrow r"></span>
  <form class="quote">
    <h3>REQUEST A FREE QUOTE</h3>
    <div class="field"><span>Name</span><i></i></div>
    <div class="field"><span>Phone</span><i></i></div>
    <div class="field"><span>Email</span><i></i></div>
    <div class="field"><span>Budget</span><i></i></div>
    <label>Project Details</label>
    <div class="area"></div>
    <span class="submit">Submit</span>
  </form>
</section>

<section class="cards">
  <article class="card">
    <div class="card-art"><div role="img" aria-label="Illustration of a house with rooftop solar" style="background:linear-gradient(#6fb3e0,#3f8f1f)"></div></div>
    <h4>Pearth Residential Solar Power</h4>
    <p>Rooftop systems sized for your household, installed by our own trained crew and backed by long warranties.</p>
    <span class="more">Read More</span>
  </article>
  <article class="card">
    <div class="card-art"><div role="img" aria-label="Illustration of commercial buildings" style="background:linear-gradient(#9fc7e8,#5c6b7a)"></div></div>
    <h4>Pearth Commercial Solar Power</h4>
    <p>Cut operating costs with panel arrays designed for offices, warehouses and retail sites across the metro area.</p>
    <span class="more">Read More</span>
  </article>
  <article class="card">
    <div class="card-art"><div role="img" aria-label="Illustration of an air conditioning unit" style="background:linear-gradient(#d8d8d8,#8a8a8a)"></div></div>
    <h4>Air Conditioning WA</h4>
    <p>Efficient split and ducted units that pair with solar power to keep running costs low all year.</p>
    <span class="more">Read More</span>
  </article>
  <article class="card">
    <div class="card-art"><div role="img" aria-label="Illustration of LED light bulbs" style="background:linear-gradient(#f4e27a,#d86a3a)"></div></div>
    <h4>Pearth LED Lighting</h4>
    <p>Bright, long lasting LED fittings for homes and workplaces that use a fraction of the energy.</p>
    <span class="more">Read More</span>
  </article>
</section>

<section class="welcome">
  <div class="welcome-copy">
    <h2>Welcome to Our Website</h2>
    <p>We design and install solar power systems for homes and businesses throughout Western Australia. Every project is handled by our own employees, from the first site visit to final connection, so you always know who is on your roof and who to call.</p>
    <p>Our team has helped thousands of families and companies lower their power bills while building a cleaner image. Ask us about rebates, finance options and the right system size for your property, and we will prepare a clear written quote within two business days.</p>
  </div>
  <div class="testimonial">
    <h5>Testimonials</h5>
    <div class="video" role="img" aria-label="Video of a customer giving a testimonial"></div>
    <div class="controls"><b></b><i></i></div>
  </div>
</section>

<section class="promo">
  <div class="services">
    <h4>Primary Products/ Services</h4>
    <ul>
      <li>Residential solar panels</li><li>Commercial solar systems</li><li>Solar hot water</li><li>Battery storage</li><li>LED lighting upgrades</li><li>Air conditioning</li><li>System maintenance</li><li>Energy audits</li>
    </ul>
  </div>
  <div class="cta" style="left:290px">
    <div class="cta-circle"><span class="small">Become a</span><span class="big">MEMBER</span></div>
    <span class="cta-btn">Click Here</span>
  </div>
  <div class="cta" style="left:430px">
    <div class="cta-circle"><span class="small">Get a</span><span class="big">FREE</span><span class="small">Quote!</span></div>
    <span class="cta-btn">Click Here</span>
  </div>
  <div class="contact">
    <p>If you would like more information on any of our products or services please contact us, we would love to hear from you!</p>
    <p><b>Phone:</b> (08) 6100 4821<br><b>Fax:</b> (08) 6100 4822<br><b>Email:</b> info@brightmeadowenergy.com.au</p>
    <p><b>Address:</b><br>7/14 Harlow Road<br>Canning Vale, WA 6155</p>
  </div>
</section>

<footer class="footer">Copyright © 2024 Bright Meadow. All rights reserved. Solar systems and energy solutions for Perth homes and businesses.</footer>
</body>
</html>
```